Local Roofing/Construction company business needs new biz card design

We need a new business card design, current cards are from the start of this operation and generic at best. We are a local Construction Company (General Contractor) with a majority of our work originating from insurance claims-exterior finish work is the main focus (Roofs-Siding-Gutters etc). Heavily involved with homeowners and the low ball offers they receive from insurance company's after a insurable event takes place. I have attached some of our original logo file(s) below.

```html
<!DOCTYPE html>
<html lang="en">
<head>
<meta charset="utf-8">
<title>Bracken Build – Business Card</title>
<link href="https://fonts.googleapis.com/css2?family=Montserrat:wght@500;600;800&display=swap" rel="stylesheet">
<style>
  :root {
    --bg: #d9d9d9;
    --green-light: #8fd4a1;
    --green: #57b972;
    --green-deep: #4aae63;
    --ink: #10202a;
    --card-white: #f1f1f1;
    --text-grey: #6a6a6a;
  }
  * { box-sizing: border-box; margin: 0; padding: 0; }
  html, body { width: 1200px; height: 1200px; overflow: hidden; }
  body {
    background: var(--bg);
    font-family: "Montserrat", sans-serif;
    position: relative;
  }
  .card {
    position: absolute;
    left: 180px;
    width: 840px;
    height: 480px;
    border-radius: 28px;
    box-shadow: 0 10px 24px rgba(0,0,0,0.18);
    overflow: hidden;
  }
  .card-front {
    top: 90px;
    background: linear-gradient(100deg, var(--green-light) 0%, var(--green) 75%);
    display: flex;
    align-items: center;
    justify-content: center;
  }
  .card-back {
    top: 630px;
    background: linear-gradient(100deg, #f6f6f6 0%, #e9e9e9 100%);
  }
  .brand {
    display: flex;
    align-items: center;
    gap: 22px;
  }
  .brand-square {
    width: 64px;
    height: 64px;
    border-radius: 10px;
  }
  .brand-name {
    font-weight: 800;
    text-transform: uppercase;
    letter-spacing: 1px;
  }
  .card-front .brand-square { background: var(--ink); }
  .card-front .brand-name { color: var(--ink); font-size: 62px; }

  .back-brand {
    position: absolute;
    left: 60px;
    top: 0;
    height: 480px;
    width: 300px;
    display: flex;
    flex-direction: column;
    align-items: center;
    justify-content: center;
    gap: 20px;
  }
  .back-brand .brand-square { background: var(--green); width: 120px; height: 120px; border-radius: 22px; }
  .back-brand .brand-name { color: var(--green); font-size: 34px; text-align: center; line-height: 1.1; }

  .divider {
    position: absolute;
    left: 400px;
    top: 120px;
    width: 2px;
    height: 240px;
    background: var(--ink);
  }
  .details {
    position: absolute;
    left: 440px;
    top: 112px;
    color: var(--text-grey);
  }
  .person-name { color: var(--green-deep); font-weight: 800; font-size: 36px; }
  .person-title { font-size: 20px; font-weight: 500; margin-top: 4px; }
  .address { font-size: 20px; font-weight: 500; margin-top: 16px; line-height: 1.35; }
  .contacts { list-style: none; margin-top: 14px; font-size: 20px; font-weight: 500; }
  .contacts li { display: flex; align-items: center; gap: 12px; line-height: 1.6; }
  .contacts svg { width: 18px; height: 18px; fill: var(--green-deep); flex: none; }
</style>
</head>
<body>

<section class="card card-front">
  <div class="brand">
    <span class="brand-square"></span>
    <span class="brand-name">Bracken Build</span>
  </div>
</section>

<section class="card card-back">
  <div class="back-brand">
    <span class="brand-square"></span>
    <span class="brand-name">Bracken<br>Build</span>
  </div>
  <div class="divider"></div>
  <div class="details">
    <h1 class="person-name">Marcus Dell</h1>
    <p class="person-title">Founder &amp; Director</p>
    <p class="address">4170 Alder Lane<br>Fairview Ohio 44210</p>
    <ul class="contacts">
      <li>
        <svg viewBox="0 0 24 24"><path d="M6.6 10.8a15.1 15.1 0 0 0 6.6 6.6l2.2-2.2c.3-.3.7-.4 1-.2 1.1.4 2.3.6 3.6.6.6 0 1 .4 1 1V20c0 .6-.4 1-1 1A17 17 0 0 1 3 4c0-.6.4-1 1-1h3.5c.6 0 1 .4 1 1 0 1.3.2 2.5.6 3.6.1.3 0 .7-.2 1z"/></svg>
        (555)-014-2270
      </li>
      <li>
        <svg viewBox="0 0 24 24"><path d="M2 5h20v14H2z M2 5l10 7 10-7" fill-rule="evenodd"/><path d="M2 6.5l10 7 10-7V5L12 12 2 5z" fill="#fff"/></svg>
        info@brackenbuild.com
      </li>
      <li>
        <svg viewBox="0 0 24 24"><path d="M12 2a10 10 0 1 0 0 20 10 10 0 0 0 0-20zm6.9 6h-3a15 15 0 0 0-1.3-3.9A8 8 0 0 1 18.9 8zM12 4c.8 1.2 1.5 2.5 1.9 4h-3.8c.4-1.5 1.1-2.8 1.9-4zM4.3 14a8 8 0 0 1 0-4h3.4a16 16 0 0 0 0 4zm.8 2h3a15 15 0 0 0 1.3 3.9A8 8 0 0 1 5.1 16zm3-8h-3a8 8 0 0 1 4.3-3.9C8.9 5.3 8.4 6.6 8.1 8zM12 20c-.8-1.2-1.5-2.5-1.9-4h3.8c-.4 1.5-1.1 2.8-1.9 4zm2.3-6H9.7a14 14 0 0 1 0-4h4.6a14 14 0 0 1 0 4zm.3 5.9c.6-1.2 1-2.5 1.3-3.9h3a8 8 0 0 1-4.3 3.9zm1.7-5.9a16 16 0 0 0 0-4h3.4a8 8 0 0 1 0 4z"/></svg>
        www.brackenbuild.com
      </li>
    </ul>
  </div>
</section>

</body>
</html>
```